Domestic violence resource cards for distribution to at-risk patients in an emergency department

Using the attached image(or very similar) and text document, a tri-fold business card is requested that integrates the image on the outside and the document content throughout the card's remaining faces. A creative format is requested, one that does not look like the typical cold, uncaring bullet point outlines that are found in similar resource projects. Bold or larger font sizes are requested for headings and body text is not required to be aligned or justified and the bullet points in the supplied document can be removed for creative license. Palattes should be clear, avoiding neons or implied target gender. Legibility is paramount, but again a creative presentation of a very serious subject is our goal. These cards are intended to be distributed to patients or others in the emergency department that may benefit from domestic violence resources. The business card size is mandatory so that the card can be concealed if needed by the receiver.
Updates

Reason: There are several revisions from designers that we are anxiously awaiting; we want to provide time for these designers to submit new designs but also continue spending time with their families and friends around the holiday season.

Target Market(s)

Patients and family in contact with emergency services

Industry/Entity Type

Healthcare

Contact Information for Business Card

Double sided tri-fold card with image on outer sides, text content and resource phone numbers on the exterior. When complete, the card should fold to standard US business card size.

Font styles to use
Other font styles liked:
• Designer's choice, but clear and legible

Requirements
Must have
• See above description. Card must be tri-fold, fold down to standard business card size, remain easily readable, and fold along the long edge.
Should not have
• Cartoon images; bloated fonts or clipart; bright, flashy neon or rainbow-like colors; additional graphics or charts.

```html
<!DOCTYPE html>
<html lang="en">
<head>
<meta charset="utf-8">
<title>Break the Silence – Resource Card</title>
<link href="https://fonts.googleapis.com/css2?family=Roboto+Condensed:ital,wght@0,400;0,500;0,700;1,400;1,500&family=Archivo+Black&display=swap" rel="stylesheet">
<style>
  :root{
    --sheet:#e9f3e2;
    --row:#ffffff;
    --red:#d8262b;
    --green:#3aa635;
    --green-dark:#238a2a;
    --ink:#1d1d1d;
    --rule:#c9d6c3;
    --night:#000000;
    --bg:#f2efe9;
  }
  *{box-sizing:border-box;margin:0;padding:0}
  html,body{width:1200px;height:837px;overflow:hidden;background:var(--bg)}
  body{position:relative;font-family:"Roboto Condensed",Arial,sans-serif;color:var(--ink)}

  .card{position:absolute;top:46px;width:423px;height:744px;background:var(--sheet);box-shadow:0 2px 8px rgba(0,0,0,.25)}
  .card--inside{left:176px}
  .card--outside{left:616px}

  .panel{position:absolute;left:0;width:100%;height:248px}
  .panel + .panel{border-top:1px solid var(--rule)}
  .panel--1{top:0}.panel--2{top:248px}.panel--3{top:496px}

  .heading{color:var(--red);font-weight:700;text-align:center;font-size:22px;letter-spacing:.1px}
  .subheading{color:var(--green-dark);font-weight:700;text-align:center;font-size:17.5px;margin-top:3px}

  .list{list-style:none;display:flex;flex-direction:column}
  .list li{display:flex;align-items:center;font-size:11.4px;line-height:13.6px;font-weight:500}
  .list li::before{content:"";flex:none;align-self:stretch}
  .list li span{flex:1;background:var(--row);padding:2px 5px}

  .list--warn{margin:10px 0 0 42px;width:338px;gap:4px}
  .list--warn li::before{width:9px;margin-right:6px;background:var(--red);margin-top:3px;margin-bottom:3px}
  .list--warn li span{padding:2px 4px}
  .panel--1 .heading{padding-top:18px}
  .verdict{color:var(--red);font-style:italic;font-weight:500;text-align:center;font-size:13px;margin-top:6px}

  .panel--2 .heading{padding-top:22px}
  .list--tips{margin:13px 0 0 20px;width:380px;gap:5px}
  .list--tips li::before{width:11px;margin-right:6px;background:var(--green)}
  .list--tips li span{padding:2px 4px}
  .panel--3 .list--tips{margin-top:10px;gap:5px}

  .remember .heading{padding-top:21px;font-size:23px}
  .list--remember{margin:10px 0 0 50px;width:324px;gap:6px}
  .list--remember li{font-size:12.6px;line-height:16px}
  .list--remember li::before{width:9px;margin-right:8px;background:var(--green)}
  .list--remember li span{padding:3px 9px}

  .directory{transform:rotate(180deg);padding:8px 27px 0 28px}
  .directory-grid{display:grid;grid-template-columns:176px 176px;column-gap:16px;row-gap:8px}
  .directory-col{display:flex;flex-direction:column;gap:8px}
  .directory-col--right{padding-top:0}
  .contact{background:var(--row);border-radius:6px;text-align:center;padding:3px 4px 2px;height:36px;display:flex;flex-direction:column;justify-content:center}
  .contact--tall{height:52px}
  .contact-name{color:var(--red);font-size:9.6px;line-height:11px}
  .contact-number{font-size:17px;font-weight:500;line-height:18px;letter-spacing:.3px}
  .contact-note{color:var(--red);font-size:9.6px;line-height:11px}
  .directory-url{text-align:center;font-weight:700;font-size:11px;margin-top:14px;letter-spacing:.2px}

  .cover{position:absolute;left:0;top:496px;width:100%;height:248px;background:var(--night)}
  .cover-photo{position:absolute;left:64px;top:18px;width:150px;height:220px;
    background:radial-gradient(ellipse at 45% 45%,#d9d9d9 0%,#8a8a8a 35%,#2a2a2a 70%,#000 100%)}
  .cover-title{position:absolute;left:271px;top:30px;font-family:"Archivo Black",Arial,sans-serif;color:var(--red);font-size:33px;line-height:40px}
  .cover-url{position:absolute;left:265px;top:198px;color:#fff;font-size:12.6px}
</style>
</head>
<body>

<section class="card card--inside">
  <div class="panel panel--1">
    <h2 class="heading">Does Your Partner Ever...</h2>
    <ul class="list list--warn">
      <li><span>Hit, kick, push, choke or slap you?</span></li>
      <li><span>Intimidate you with weapons or harmful objects?</span></li>
      <li><span>Force you to engage in sexual acts?</span></li>
      <li><span>Threaten to hurt you, your children or your friends/family?</span></li>
      <li><span>Threaten to deport you or tell others your personal information?</span></li>
      <li><span>Control where you go, who you talk to or who you make friends with?</span></li>
      <li><span>Keep, hide or destroy your most important things?</span></li>
      <li><span>Blame, embarrass, or criticize you, make you feel worthless or guilty?</span></li>
      <li><span>Control your food, money, medicines or medical care?</span></li>
    </ul>
    <p class="verdict">You may be a victim of abuse or neglect!</p>
  </div>

  <div class="panel panel--2">
    <h2 class="heading">Leaving can be Tough and very Dangerous.</h2>
    <p class="subheading">Here are some tips to help you plan for safety:</p>
    <ul class="list list--tips">
      <li><span>Know people you can talk to and ask them to call the police if they hear a disturbance coming from your home</span></li>
      <li><span>Teach your children how to contact the police or fire department</span></li>
      <li><span>Practice how to get you and your children out of your home quickly and safely</span></li>
      <li><span>Plan where you will go if you have to leave right away and know the location of local emergency shelters</span></li>
      <li><span>Leave copies of important papers, keys, cash, IDs, and medicine with a friend or relative you trust</span></li>
    </ul>
  </div>

  <div class="panel panel--3">
    <ul class="list list--tips">
      <li><span>Have a small bag packed and ready at a friend or relative’s house so you can leave quick</span></li>
      <li><span>Stay off social media or cancel you accounts so that you can’t be found online or through your friends</span></li>
      <li><span>Do not talk about your plans in public areas or in mixed groups</span></li>
      <li><span>Open a credit card or bank account in your name only and do not use it until you are ready</span></li>
      <li><span>Keep a chargedprepaid cell phone and a shelter hotline number ready for emergencies</span></li>
      <li><span>Review your plan often and only share with trusted friends or family</span></li>
      <li><span>Be careful: you are at most risk during the first 72 hours after leaving an abusive situation</span></li>
      <li><span>Seek help at a police station, firehouse or hospital if needed</span></li>
    </ul>
  </div>
</section>

<section class="card card--outside">
  <div class="panel panel--1 remember">
    <h2 class="heading">Always Remember</h2>
    <ul class="list list--remember">
      <li><span>You have a right to be safe anywhere</span></li>
      <li><span>You don’t deserve to be hit or threatened</span></li>
      <li><span>Your children deserve to grow up without violence</span></li>
      <li><span>You have a right to protect you or your children until you are out of danger</span></li>
      <li><span>You are not alone</span></li>
      <li><span>You have choices</span></li>
    </ul>
  </div>

  <div class="panel panel--2 directory">
    <div class="directory-grid">
      <div class="directory-col">
        <div class="contact"><p class="contact-name">Harbor Line National Support</p><p class="contact-number">1-800-555-0142</p></div>
        <div class="contact"><p class="contact-name">Northgate Family Safety Resources</p><p class="contact-number">303-555-0118</p></div>
        <div class="contact"><p class="contact-name">Oak Circle Violence Resources</p><p class="contact-number">303-555-0163</p></div>
        <div class="contact"><p class="contact-name">The Lantern Crisis Line</p><p class="contact-number">1-888-555-0190</p></div>
      </div>
      <div class="directory-col directory-col--right">
        <div class="contact contact--tall"><p class="contact-name">Safe Haven Metro:<br>Domestic Violence Crisis Resource</p><p class="contact-number">303-555-0127</p></div>
        <div class="contact contact--tall"><p class="contact-name">Quiet Bench:<br>Sexual Assault Victim’s Advocate</p><p class="contact-number">303-555-0174</p></div>
        <div class="contact contact--tall"><p class="contact-name">Respect First: Teen Dating Resource</p><p class="contact-number">1-866-555-0136</p><p class="contact-note">or text “respect” to 55512</p></div>
      </div>
    </div>
    <p class="directory-url">www.shelterpath.org</p>
  </div>

  <div class="cover">
    <div class="cover-photo" role="img" aria-label="Black and white photograph of one hand tightly gripping another person's wrist"></div>
    <h1 class="cover-title">Break<br>the<br>Silence</h1>
    <p class="cover-url">www.shelterpath.org</p>
  </div>
</section>

</body>
</html>
```